Business Card Design Project

1. Show the company logo.
2. Only company email ID and website address to be shown (office@tikhayavolna.fm , www.tikhayavolna.fm).
3. Logo to be provided by us, 2 designs just in case. The logo is made with ' Tikhaya Volna' text, need to be edited so that it shows 'Yasnaya Afisha' instead .
4. Single sided business card, portrait or landscape is not a problem; back side to be filled with colors or a design that matches the logo the best.
5. Logo is to be embossed.
6. We're looking at an English and Russian version.
7. any other better idea is always welcomed.

```html
<!DOCTYPE html>
<html lang="en">
<head>
<meta charset="utf-8">
<title>Yasnaya Afisha — Business Card</title>
<link rel="stylesheet" href="https://fonts.googleapis.com/css2?family=Arimo:wght@400;700&display=swap">
<style>
  :root {
    --sky-top: #4479c2;
    --sky-bottom: #2c5ca9;
    --navy-top: #272f70;
    --navy-bottom: #18204f;
    --badge: #1e3a70;
    --badge-edge: #2d4d8a;
    --name: #d6e6fb;
    --amber: #f2a82a;
    --rust: #8b3423;
    --bubble: #8a84b4;
    --contact: #ebe6ee;
    --trim-red: #e0463c;
    --trim-green: #5caa4a;
  }
  html, body {
    margin: 0;
    padding: 0;
    width: 1200px;
    height: 781px;
    overflow: hidden;
    background: #ffffff;
  }
  .card {
    position: relative;
    width: 1200px;
    height: 781px;
    overflow: hidden;
    font-family: "Arimo", Arial, sans-serif;
    background: linear-gradient(180deg, var(--navy-top) 0%, var(--navy-bottom) 100%);
  }
  .card__sky {
    position: absolute;
    left: 0; top: 0;
    width: 1200px; height: 388px;
    background: linear-gradient(180deg, var(--sky-top) 0%, var(--sky-bottom) 100%);
  }
  .card__navy {
    position: absolute;
    left: 0; top: 388px;
    width: 1200px; height: 393px;
    background: linear-gradient(180deg, var(--navy-top) 0%, var(--navy-bottom) 100%);
  }
  .card__bubbles {
    position: absolute;
    left: 0; bottom: 0;
    width: 700px; height: 220px;
    background: radial-gradient(ellipse at 35% 80%, rgba(138,132,180,0.45) 0%, rgba(138,132,180,0.18) 45%, rgba(138,132,180,0) 75%);
  }
  .card__wedge {
    position: absolute;
    left: 0; top: 0;
    width: 1200px; height: 781px;
  }
  .brand {
    position: absolute;
    left: 25px; top: 25px;
    width: 326px; height: 326px;
  }
  .brand__disc {
    position: absolute;
    left: 0; top: 0;
    width: 326px; height: 326px;
    border-radius: 50%;
    background: radial-gradient(circle at 40% 35%, var(--badge-edge) 0%, var(--badge) 70%);
  }
  .brand__name {
    position: absolute;
    left: 30px; top: 140px;
    width: 266px;
    margin: 0;
    text-align: center;
    font-size: 30px;
    font-weight: 700;
    letter-spacing: 1px;
    line-height: 1.2;
    color: var(--name);
  }
  .contact {
    position: absolute;
    right: 42px; top: 618px;
    margin: 0;
    text-align: right;
    font-size: 33px;
    font-weight: 700;
    line-height: 43px;
    color: var(--contact);
    font-style: normal;
  }
  .trim {
    position: absolute;
    pointer-events: none;
    box-sizing: border-box;
  }
  .trim--bleed { left: 6px; top: 6px; right: 6px; bottom: 6px; border: 1px solid var(--trim-red); }
  .trim--safe { left: 13px; top: 13px; right: 13px; bottom: 13px; border: 1px solid var(--trim-green); }
</style>
</head>
<body>
  <main class="card">
    <div class="card__sky"></div>
    <div class="card__navy"></div>
    <div class="card__bubbles" role="img" aria-label="Decorative pattern of concentric bubble rings in soft lavender"></div>

    <svg class="card__wedge" width="1200" height="781" viewBox="0 0 1200 781" aria-hidden="true">
      <defs>
        <linearGradient id="wedge-fill" x1="0" y1="0" x2="0" y2="1">
          <stop offset="0" stop-color="var(--amber)" stop-opacity="0.95"/>
          <stop offset="0.5" stop-color="#d88a3a" stop-opacity="0.85"/>
          <stop offset="1" stop-color="var(--rust)" stop-opacity="0.92"/>
        </linearGradient>
      </defs>
      <polygon points="1200,0 1200,781 676,781" fill="url(#wedge-fill)"/>
    </svg>

    <div class="brand">
      <div class="brand__disc"></div>
      <p class="brand__name">Yasnaya Afisha</p>
    </div>

    <address class="contact">
      Our address :<br>
      office@tikhayavolna.fm<br>
      www.tikhayavolna.fm
    </address>

    <div class="trim trim--bleed"></div>
    <div class="trim trim--safe"></div>
  </main>
</body>
</html>
```